Stationary for New Company

We need stationary designed for a new company. Details of the required stationary is attached.

The final version should be trendy, clean... only 2 colours (green + grey/black) and professional.

#1: Business Cards (design on 2 sides)
#2: Letterhead (word format)
#3: Cover Page and back cover for proposals
#4: Envelopes,
#5: Thank You card,
#6: Presentation Folder,
#7: Email signatures template (sample attached in word document)

Logo is attached. Logo can be reversed out (will attach once available). Logo can be stacked or horizontal (provided as horizontal).

Files need to be provided in ai + png format.

Target Market(s)

Business owners. More affluent.

Industry/Entity Type

Business

Requirements
Must have
• See brief

Font: Calibri
Should not have
• Photographs / stock photos

```html
<!DOCTYPE html>
<html lang="en">
<head>
<meta charset="utf-8">
<title>Parkline Insurance Brokers – Envelopes</title>
<link rel="stylesheet" href="https://fonts.googleapis.com/css2?family=Montserrat:wght@300;400;500&display=swap">
<style>
  :root {
    --backdrop: #e9eaeb;
    --paper: #fbfbfb;
    --paper-edge: #dcdddf;
    --flap-shade: #f1f1f2;
    --brand-green: #6b9a2b;
    --ink-grey: #4a4f5b;
  }
  * { box-sizing: border-box; margin: 0; padding: 0; }
  html, body {
    width: 1200px;
    height: 795px;
    overflow: hidden;
    background: var(--backdrop);
    font-family: "Montserrat", sans-serif;
  }
  .stationery {
    position: relative;
    width: 1200px;
    height: 795px;
    display: flex;
    align-items: center;
    justify-content: center;
    gap: 60px;
  }
  .envelope {
    position: relative;
    width: 520px;
    height: 260px;
    background: var(--paper);
    border: 1px solid var(--paper-edge);
    box-shadow: 0 6px 18px rgba(0, 0, 0, 0.08);
  }
  .envelope__flap {
    position: absolute;
    left: 0;
    top: 0;
    width: 100%;
    height: 92px;
  }
  .brand {
    display: flex;
    align-items: center;
    gap: 8px;
    color: var(--brand-green);
    font-weight: 300;
  }
  .brand__square {
    background: var(--brand-green);
    flex: none;
  }
  .brand__name {
    line-height: 1;
  }
  .brand__name small {
    display: block;
    font-size: 0.42em;
    letter-spacing: 0.02em;
    margin-top: 2px;
  }
  .envelope--back .brand {
    position: absolute;
    left: 50%;
    top: 30px;
    transform: translateX(-50%);
    font-size: 20px;
  }
  .envelope--back .brand__square { width: 24px; height: 24px; }
  .envelope--front .brand {
    position: absolute;
    left: 34px;
    top: 44px;
    font-size: 34px;
    gap: 12px;
  }
  .envelope--front .brand__square { width: 44px; height: 44px; }
  .return-address {
    position: absolute;
    left: 34px;
    bottom: 30px;
    font-style: normal;
    font-size: 11px;
    font-weight: 500;
    letter-spacing: 0.12em;
    line-height: 1.6;
    color: var(--ink-grey);
  }
</style>
</head>
<body>
  <main class="stationery">
    <section class="envelope envelope--back" aria-label="Envelope back">
      <svg class="envelope__flap" viewBox="0 0 520 92" preserveAspectRatio="none" aria-hidden="true">
        <path d="M0 0 H520 V72 Q520 90 502 90 H18 Q0 90 0 72 Z" fill="var(--flap-shade)" stroke="var(--paper-edge)" stroke-width="1"/>
      </svg>
      <div class="brand">
        <span class="brand__square"></span>
        <span class="brand__name">Parkline<small>Insurance Brokers</small></span>
      </div>
    </section>

    <section class="envelope envelope--front" aria-label="Envelope front">
      <div class="brand">
        <span class="brand__square"></span>
        <span class="brand__name">Parkline<small>Insurance Brokers</small></span>
      </div>
      <address class="return-address">
        4580 Cedar Ridge Ave NE<br>
        Fairview, NM 87000
      </address>
    </section>
  </main>
</body>
</html>
```